Quorvane needs a new design we have an updated logo and want a high qualitative high end feel

feel and aesthetic should be high qualitative like the packaging in a zuvi or the qualatative weight/feel of an zuvi design. modern, elegant bold.probably just the quorvane logo on the backone vesion could be blue background white letter ... open to ideas
Target Market(s)
legal, insurance , medical, finance rho 740
Industry/Entity Type
Information Technology
Font styles to use
Serif

```html
<!DOCTYPE html>
<html lang="en">
<head>
<meta charset="utf-8">
<title>Quorvane Business Card</title>
<link rel="stylesheet" href="https://fonts.googleapis.com/css2?family=Lato:wght@400;700&display=swap">
<style>
  :root {
    --navy: #1b2b3f;
    --white: #ffffff;
    --grey: #6b6b6b;
    --stage: #4a3124;
  }
  * { margin: 0; padding: 0; box-sizing: border-box; }
  html, body { width: 1200px; height: 848px; overflow: hidden; }
  body {
    background: var(--stage);
    font-family: "Lato", sans-serif;
    position: relative;
  }
  .card {
    position: absolute;
    width: 674px;
    height: 378px;
    border-radius: 22px;
    box-shadow: 0 6px 14px rgba(0,0,0,0.35);
  }
  .card-front { left: 251px; top: 28px; background: var(--navy); }
  .card-back { left: 249px; top: 441px; width: 677px; height: 374px; background: var(--white); }

  .wordmark {
    position: absolute;
    font-family: "Lato", sans-serif;
    font-weight: 700;
    line-height: 1;
    letter-spacing: 0.5px;
    white-space: nowrap;
  }
  .card-front .wordmark {
    left: 0; right: 0; top: 138px;
    text-align: center;
    font-size: 84px;
    color: var(--white);
  }
  .card-back .wordmark {
    right: 38px; top: 66px;
    font-size: 56px;
    color: var(--navy);
  }

  .holder { position: absolute; left: 39px; top: 214px; width: 600px; }
  .holder-name {
    font-size: 23px; font-weight: 700; color: var(--navy);
    letter-spacing: 0.2px; line-height: 28px;
  }
  .holder-role {
    display: flex; align-items: center; gap: 10px;
    font-size: 18px; line-height: 22px; color: var(--grey);
  }
  .holder-role::after {
    content: ""; flex: 1; height: 1.5px; background: var(--navy);
  }

  .contact-list {
    position: absolute; left: 39px; top: 274px;
    list-style: none; font-size: 18.5px; color: var(--grey);
  }
  .contact-list li { display: flex; align-items: center; gap: 7px; height: 22.5px; white-space: nowrap; }
  .contact-list svg { width: 12px; height: 12px; fill: var(--navy); flex: none; }
  .contact-list strong { font-weight: 400; color: var(--navy); }

  .address {
    position: absolute; right: 38px; top: 296px;
    text-align: right; font-style: normal; white-space: nowrap;
    font-size: 18.5px; line-height: 23px; color: var(--grey);
  }
</style>
</head>
<body>
  <section class="card card-front">
    <div class="wordmark">quorvane</div>
  </section>

  <section class="card card-back">
    <div class="wordmark">quorvane</div>

    <div class="holder">
      <div class="holder-name">MAREK HOLLIS</div>
      <div class="holder-role">President</div>
    </div>

    <ul class="contact-list">
      <li>
        <svg viewBox="0 0 12 12" aria-hidden="true"><path d="M2.5 0.5l2 2.4-1.2 1.3c.7 1.6 2 2.9 3.5 3.6l1.3-1.2 2.4 2-1.3 2.4C4.8 10.7 1.3 7.2 0.3 2.7z"/></svg>
        555.014.2276
      </li>
      <li>
        <svg viewBox="0 0 12 12" aria-hidden="true"><path d="M0 2.5h12v7H0z M0.8 3l5.2 3.6L11.2 3" stroke="#fff" stroke-width="0.9"/></svg>
        hello@northbrightmail.com
      </li>
      <li>
        <svg viewBox="0 0 12 12" aria-hidden="true"><circle cx="6" cy="6" r="5.3" fill="none" stroke="#1b2b3f" stroke-width="1.2"/><path d="M0.8 6h10.4M6 0.8v10.4" stroke="#1b2b3f" stroke-width="1"/><ellipse cx="6" cy="6" rx="2.4" ry="5.3" fill="none" stroke="#1b2b3f" stroke-width="1"/></svg>
        <span>www.<strong>quorvanegroup</strong>.com</span>
      </li>
    </ul>

    <address class="address">
      418 Harlow Street, 2nd Floor<br>
      Brookline, NY 10120
    </address>
  </section>
</body>
</html>
```